Law Firm Redesign of Stationery

We are a law firm that just expanded to our second location. We had a redesign on our logo for signage and we are now looking for a redesign of business cards (updated for our 6 current staff), letterhead, and envelopes for the new logo and include both locations. We have the Illustrator file for the new logo and the Illustrator or EPS files for all previous stationery. We would like to keep the same blue/gray color scheme but try and find a new look that matches the new logo. Our locations are in the Baltimore/D.C. metro area so something fresh, professional, and urban is the direction we would like to go in.
Industry/Entity Type
Legal
Requirements
Must have
- Must have both office addresses included: 415 Pellmore Rd, N.W., Glen Burnie, MD 21061 and 5183 Thistlebend Lane, Columbia, MD 21045. We would like to maintain the current blue and grey color scheme.

```html
<!DOCTYPE html>
<html lang="en">
<head>
<meta charset="utf-8">
<title>Harlan Reese Legal — Business Cards</title>
<link href="https://fonts.googleapis.com/css2?family=Lato:wght@300;400;700&display=swap" rel="stylesheet">
<style>
  :root {
    --firm-blue: #0b4f9e;
    --ink: #2b2b2b;
    --paper: #f6f6f4;
    --backdrop: #e6e4e0;
    --white: #ffffff;
  }
  * { box-sizing: border-box; margin: 0; padding: 0; }
  html, body { width: 1200px; height: 959px; overflow: hidden; }
  body {
    background: var(--backdrop);
    font-family: "Lato", Arial, sans-serif;
    position: relative;
  }
  .card {
    position: absolute;
    width: 560px;
    height: 320px;
    box-shadow: 0 4px 14px rgba(0,0,0,0.12);
  }

  /* Back of card */
  .card--back {
    left: 60px; top: 110px;
    background: var(--firm-blue);
    color: var(--white);
    display: flex;
    align-items: center;
    justify-content: center;
  }
  .back-firm-name {
    font-weight: 300;
    font-size: 34px;
    letter-spacing: 3px;
    white-space: nowrap;
  }

  /* Front of card */
  .card--front {
    left: 580px; top: 520px;
    background: var(--paper);
    color: var(--ink);
  }
  .front-firm-name {
    position: absolute;
    right: 34px; top: 52px;
    color: var(--firm-blue);
    font-weight: 300;
    font-size: 24px;
    letter-spacing: 2px;
    white-space: nowrap;
  }
  .front-rule {
    position: absolute;
    left: 30px; right: 30px; top: 140px;
    border-top: 1px solid var(--ink);
  }
  .attorney-name {
    position: absolute;
    left: 30px; top: 156px;
    color: var(--firm-blue);
    font-weight: 700;
    font-size: 21px;
    white-space: nowrap;
  }
  .name-rule {
    position: absolute;
    left: 30px; width: 240px; top: 190px;
    border-top: 1px solid var(--ink);
  }
  .contact-list {
    position: absolute;
    left: 30px; top: 200px;
    list-style: none;
    font-size: 12.5px;
    line-height: 19px;
  }
  .contact-list li { display: flex; align-items: center; gap: 7px; white-space: nowrap; }
  .contact-list svg { width: 12px; height: 12px; fill: var(--firm-blue); flex: none; }
  .office {
    position: absolute;
    top: 158px;
    font-size: 11.5px;
    line-height: 15px;
    font-style: normal;
    white-space: nowrap;
  }
  .office--glen-burnie { left: 284px; }
  .office--columbia { left: 424px; }
  .office-title { color: var(--firm-blue); display: block; }
</style>
</head>
<body>
  <section class="card card--back" aria-label="Business card back">
    <span class="back-firm-name">HARLAN REESE LEGAL</span>
  </section>

  <section class="card card--front" aria-label="Business card front">
    <span class="front-firm-name">HARLAN REESE LEGAL</span>
    <div class="front-rule"></div>
    <h1 class="attorney-name">Claire M. Dorsey, Esq.</h1>
    <div class="name-rule"></div>
    <ul class="contact-list">
      <li>
        <svg viewBox="0 0 12 12" aria-hidden="true"><path d="M1 4c0-2 2-3 5-3s5 1 5 3l-2 1-1-1.5H4L3 5zM3 6h6l1 5H2z"/></svg>
        410-555-0142
      </li>
      <li>
        <svg viewBox="0 0 12 12" aria-hidden="true"><path d="M3 1h6v3H3zM1 5h10v5H9v-2H3v2H1zM3 9h6v2H3z"/></svg>
        410-555-0187
      </li>
      <li>
        <svg viewBox="0 0 12 12" aria-hidden="true"><path d="M1 3h10v7H1zM1.5 3.5 6 7l4.5-3.5" stroke="#f6f6f4" stroke-width="0.8"/></svg>
        cdorsey@harlanreese.com
      </li>
      <li>
        <svg viewBox="0 0 12 12" aria-hidden="true"><circle cx="6" cy="6" r="5"/><path d="M1 6h10M6 1c-2 3-2 7 0 10M6 1c2 3 2 7 0 10" stroke="#f6f6f4" stroke-width="0.7" fill="none"/></svg>
        www.harlanreese.com
      </li>
    </ul>
    <address class="office office--glen-burnie">
      <span class="office-title">Anne Arundel Co. Office</span>
      415 Pellmore Rd, N.W.<br>
      Glen Burnie, MD 21061
    </address>
    <address class="office office--columbia">
      <span class="office-title">Howard Co. Office</span>
      5183 Thistlebend Lane<br>
      Columbia, MD 21045
    </address>
  </section>
</body>
</html>
```